Business Card Design

We need a business card design for a Non-Profit Christian Based Organization located in Milford, Pa.
Alder Ridge Helping Harbor
Is a Christ-centered organization dedicated to providing compassion and hope to homeless or near homeless, families and individuals, by meeting their basic and urgent need of food, clothing and shelter.
Updates
the logo is black and white
and must add the color green some where 00400
Industry/Entity Type
Clothing
Contact Information for Business Card
Alder Ridge Helping Harbor
P.O. Box 287
Milord, Pa 18337
Phone: (570) 413-CARE(2273)
Toll Free: (855) 413-CARE
email:Info@alderridgehh.org
email:Careline@alderridgehh.org
Our organization already has a logo.
Front of card:
Is a Christ-centered organization dedicated to providing compassion and hope to homeless or near homes, families and individual by meeting their basic and urgent need of food, clothing and shelter.(this is our Mission Statement)
On back of card:
'I was hungry and you gave me something to eat;
"I was thirsty and you gave me something to drink;
"I was a stranger and you invited me in."
Matthew 25:35
Color: Logo is black and white
Background color I would like a bright light green 00ff00(close to that)
I attached a sample of what I created on Quill Press but, I don't like the color green, nor the design (but I just wanted to give you and Idea of the Logo and Alder Ridge (one line) Helping Harbor (second line) in a different font thank you
Delia Rostova
Pr/Board of Directors

```html
<!DOCTYPE html>
<html lang="en">
<head>
<meta charset="utf-8">
<title>Alder Ridge Helping Harbor – Card Back</title>
<link rel="stylesheet" href="https://fonts.googleapis.com/css2?family=Kalam:wght@400&display=swap">
<style>
  :root {
    --card-green: #afd13a;
    --mark-green: #9fc234;
    --ink: #111111;
  }
  html, body {
    margin: 0;
    padding: 0;
    width: 1200px;
    height: 686px;
    overflow: hidden;
  }
  .card-back {
    position: relative;
    width: 1200px;
    height: 686px;
    background: var(--card-green);
    overflow: hidden;
    font-family: "Kalam", cursive;
  }
  .brand-watermark {
    position: absolute;
    left: 228px;
    top: 0;
    width: 640px;
    height: 686px;
    display: flex;
    flex-direction: column;
    justify-content: center;
    align-items: center;
    color: var(--mark-green);
    font-family: "Kalam", cursive;
    font-weight: 400;
    font-size: 104px;
    line-height: 1.15;
    text-align: center;
    white-space: nowrap;
    user-select: none;
  }
  .verse {
    position: absolute;
    left: 268px;
    top: 222px;
    margin: 0;
    color: var(--ink);
    font-size: 35px;
    font-weight: 400;
    line-height: 67px;
  }
  .verse span {
    display: block;
  }
</style>
</head>
<body>
  <div class="card-back">
    <div class="brand-watermark" aria-hidden="true">
      <span>Alder Ridge</span>
      <span>Helping Harbor</span>
    </div>
    <p class="verse">
      <span>I was hungry and you gave me something to eat</span>
      <span>I was thirsty and you gave me something to drink.</span>
      <span>I was a stranger and you invited me in.</span>
    </p>
  </div>
</body>
</html>
```